Varnok Develoipment and Management Corp Web Design Project

Website... Based on logo. Update forthcoming....
Updates

Reason: Extended to include recently completed logo design.

Target Market(s)

Financiers, investors, public officials, and landowners.

Industry/Entity Type

Management

Requirements
Should not have
• No palm trees, mayan ruins, or other Caribbean references.

```html
<!DOCTYPE html>
<html lang="en">
<head>
<meta charset="utf-8">
<title>Varnok — Development and Management Corp</title>
<link rel="stylesheet" href="https://fonts.googleapis.com/css2?family=Raleway:wght@400;500;600&family=Roboto:ital,wght@0,300;0,400;1,300&family=Lora:ital@1&display=swap">
<style>
:root{
  --green:#a4bf3a;
  --blue:#2389c0;
  --link:#2a8fc4;
  --ink:#333;
  --text:#7a7a7a;
  --muted:#8c8c8c;
  --rule:#d9d9d9;
  --band:#f6f6f6;
  --footer:#262626;
}
*{margin:0;padding:0;box-sizing:border-box}
html,body{width:891px;height:1200px;overflow:hidden;background:#fff}
body{font-family:"Roboto",sans-serif;color:var(--text)}
.page{position:relative;width:891px;height:1200px;overflow:hidden}
.abs{position:absolute}
.raleway{font-family:"Raleway",sans-serif}

/* header */
.brand{left:88px;top:22px;display:flex;align-items:center;gap:8px}
.brand-mark{width:36px;height:38px;background:var(--green)}
.brand-name{font-family:"Raleway",sans-serif;font-weight:600;font-size:21px;color:var(--green);letter-spacing:1px;line-height:1}
.brand-tag{font-size:5.5px;color:var(--muted);margin-top:3px}
.main-nav{top:35px;left:426px;display:flex;gap:16px;font-family:"Raleway",sans-serif;font-size:13px;color:#555}
.main-nav .active{color:#222;text-decoration:underline;text-underline-offset:3px}

/* hero */
.hero{left:0;top:75px;width:891px;height:277px;background:linear-gradient(180deg,#3a3d42 0%,#4b4b4c 45%,#2f3034 100%)}
.hero::before{content:"";position:absolute;inset:0;background:radial-gradient(circle at 22% 50%,rgba(190,140,70,.35),transparent 35%)}
.hero-title{left:0;width:891px;top:50px;text-align:center;font-family:"Raleway",sans-serif;font-weight:600;font-size:38px;color:#fff}
.hero-sub{left:0;width:891px;top:112px;text-align:center;font-family:"Raleway",sans-serif;font-size:14.5px;line-height:24px;color:#fff}
.hero-btn{left:370px;top:206px;width:151px;height:37px;background:var(--green);color:#fff;border-radius:3px;font-family:"Raleway",sans-serif;font-weight:600;font-size:16px;display:flex;align-items:center;justify-content:center}
.hero-arrow{top:118px}

/* welcome */
.welcome-band{left:0;top:352px;width:891px;height:218px;background:var(--band)}
.section-title{font-family:"Raleway",sans-serif;font-size:22px;color:#555;font-weight:400}
.section-title b{font-weight:500;color:#333}
.underline{height:1px;background:#ccc}
.welcome-text{left:89px;top:450px;width:460px;font-size:12.8px;line-height:20px;color:var(--text)}
.tweet{left:631px;width:150px}
.tweet-icon{position:absolute;left:0;top:2px;width:15px;height:15px;border-radius:50%;border:1px solid #9ecde6;background:#fff}
.tweet p{margin-left:27px;font-size:6.5px;line-height:9.5px;color:var(--muted)}
.tweet em{display:block;margin-left:27px;margin-top:3px;font-size:6.5px;color:var(--green)}

/* blog */
.small-title{font-family:"Raleway",sans-serif;font-size:16px;color:#666}
.pager{display:flex;gap:3px}
.pager span{width:15px;height:15px;border-radius:50%;background:#aaa}
.blog-img{left:88px;top:649px;width:176px;height:133px;background:linear-gradient(180deg,#4d8fd2 0%,#9cc4e8 40%,#b9a58d 62%,#a46a4d 100%)}
.blog-title{left:290px;top:648px;font-family:"Raleway",sans-serif;font-size:16px;color:#555}
.blog-text{left:290px;top:672px;width:215px;font-size:11.6px;line-height:19.2px;color:var(--muted)}

.news{left:574px;top:618px;width:218px;height:182px;border:1px solid #ddd;background:var(--band)}
.news-head{height:38px;background:var(--blue);color:#fff;font-family:"Raleway",sans-serif;font-size:17px;padding:8px 0 0 18px}
.news-head b{font-weight:600}
.news-item{position:absolute;left:9px;width:195px}
.news-thumb{position:absolute;left:0;top:0;width:43px;height:39px;background:linear-gradient(160deg,#d9c9a8,#d64e2a 55%,#3b3a3c)}
.news-item h4{margin-left:54px;font-weight:400;font-size:9.6px;color:var(--link)}
.news-item p{margin-left:54px;margin-top:4px;font-size:5.8px;line-height:8.6px;color:#777}
.news-item p a{color:var(--blue);font-weight:400;text-decoration:none}
.news-sep{left:9px;width:194px;top:106px;height:1px;background:#d6d6d6}

/* lower row */
.short-line{width:26px;height:1px;background:#ccc}
.faq-text{left:92px;width:152px;font-size:8.8px;line-height:15px;color:#777}
.faq-text a{color:var(--link)}
.faq-sep{left:88px;width:150px;height:1px;background:#ccc}
.nl-text{left:318px;top:918px;width:200px;font-size:11.5px;line-height:15px;color:#555}
.nl-text span{color:var(--link)}
.field{left:318px;width:190px;height:25px;border:1px solid var(--green);background:#fff;font-style:italic;font-size:9px;color:#888;padding:6px 9px}
.field svg{position:absolute;right:9px;top:7px}
.subscribe{left:319px;top:1061px;width:72px;height:24px;background:var(--green);color:#fff;font-family:"Raleway",sans-serif;font-size:12px;border-radius:2px;display:flex;align-items:center;justify-content:center}
.avatar{width:44px;height:44px;border-radius:50%;border:1px solid #ddd;background:linear-gradient(180deg,#e9e9e9,#bfc3c8)}
.quote{left:625px;width:135px}
.quote .mark{position:absolute;left:0;top:-6px;font-family:"Lora",serif;font-size:16px;color:var(--blue)}
.quote p{margin-left:13px;font-family:"Lora",serif;font-style:italic;font-size:7.3px;line-height:10.4px;color:#777}
.quote .who{margin-top:5px;text-align:right;font-size:7.3px;color:#555}
.quote .who span{color:var(--link)}
.t-sep{left:573px;width:186px;height:1px;background:#ccc}

/* footer */
.footer{left:0;top:1122px;width:891px;height:78px;background:var(--footer)}
.foot-nav{left:85px;top:18px;display:flex;gap:16px;font-family:"Raleway",sans-serif;font-size:13px;color:#fff}
.copy{left:87px;top:45px;font-size:9.8px;color:#ccc}
.social{left:651px;top:23px;display:flex;gap:12px}
.social span{width:26px;height:26px;border-radius:50%;border:1.5px solid #fff}
</style>
</head>
<body>
<div class="page">

  <header>
    <div class="abs brand">
      <div class="brand-mark"></div>
      <div>
        <div class="brand-name">VARNOK</div>
        <div class="brand-tag">Develoipment and Management Corp</div>
      </div>
    </div>
    <nav class="abs main-nav">
      <span class="active">Home</span><span>Services</span><span>Our Team</span><span>Insight Articles</span><span>Contact Us</span>
    </nav>
  </header>

  <section class="abs hero" role="img" aria-label="City skyline with glass office towers at dusk">
    <h1 class="abs hero-title">SIMPLE. GOOD DESIGN.</h1>
    <p class="abs hero-sub">This is sample text only. Lorem ipsum dolor sit amet,<br>consectetur adipisicing elit, sed do eiusmod.</p>
    <div class="abs hero-btn">LEARN MORE</div>
    <svg class="abs hero-arrow" style="left:36px" width="38" height="38" viewBox="0 0 38 38"><circle cx="19" cy="19" r="17.5" fill="none" stroke="#cfcfcf" stroke-width="2"/><path d="M25 11 L11 19 L25 27 L21 19 Z" fill="#cfcfcf"/></svg>
    <svg class="abs hero-arrow" style="left:803px" width="38" height="38" viewBox="0 0 38 38"><circle cx="19" cy="19" r="17.5" fill="none" stroke="#cfcfcf" stroke-width="2"/><path d="M13 11 L27 19 L13 27 L17 19 Z" fill="#cfcfcf"/></svg>
  </section>

  <section>
    <div class="abs welcome-band"></div>
    <h2 class="abs section-title" style="left:88px;top:398px">Welcome to <b>Varnok</b></h2>
    <div class="abs underline" style="left:88px;top:433px;width:67px"></div>
    <p class="abs welcome-text">Culpa qui officia deserunt mollit anim id est laborum. Sed ut perspiciatis unde omnis iste natus error sit voluptatem accusantium doloremque laudantium, totam rem aperiam, eaque ipsa quae ab illo inventore veritatis et quasi archi tecto beatae vitae dicta sunt explicabo.</p>

    <h2 class="abs section-title" style="left:630px;top:398px">Latest <b>Tweets</b></h2>
    <div class="abs underline" style="left:631px;top:433px;width:33px"></div>
    <div class="abs tweet" style="top:453px"><span class="tweet-icon"></span><p>Eiusmod tempor incididunt ut labore et dolore magna aliqua.</p><em>About 3 hours ago</em></div>
    <div class="abs tweet" style="top:499px"><span class="tweet-icon"></span><p>Ut enim ad minim veniam, quis nostrud exercitation.</p><em>About 4 hours ago</em></div>
  </section>

  <section>
    <h3 class="abs small-title" style="left:88px;top:608px">Blog</h3>
    <div class="abs pager" style="left:477px;top:613px"><span></span><span></span></div>
    <div class="abs underline" style="left:88px;top:637px;width:422px;background:#bbb"></div>
    <div class="abs blog-img" role="img" aria-label="Aerial view of a city with red rooftops under a blue sky"></div>
    <h4 class="abs blog-title">Title of article here</h4>
    <p class="abs blog-text">Consectetur adipisicing elit, sed do eiusmod tempor incididunt ut labore et dolore magna aliqua. Ut enim ad minim veniam, quis nostrud exercita tion ullamco laboris nisi ut aliquip ex ea commodo.</p>

    <div class="abs news">
      <div class="news-head">Latest <b>News &amp; Events</b></div>
      <div class="news-item" style="top:51px">
        <div class="news-thumb" role="img" aria-label="Hot air balloon photo"></div>
        <h4>Lorem ipsum doloreum</h4>
        <p>Lorem ipsum dolor sit amet, consectetur adipisicing elit, sed do eiusmod tempor incididunt ut labore et dol... <a>[Read More]</a></p>
      </div>
      <div class="abs news-sep"></div>
      <div class="news-item" style="top:119px">
        <div class="news-thumb" role="img" aria-label="Hot air balloon photo"></div>
        <h4>Lorem ipsum doloreum</h4>
        <p>Lorem ipsum dolor sit amet, consectetur adipisicing elit, sed do eiusmod tempor incididunt ut labore et dol... <a>[Read More]</a></p>
      </div>
    </div>
  </section>

  <section>
    <h3 class="abs small-title" style="left:89px;top:870px">FAQ</h3>
    <div class="abs short-line" style="left:89px;top:898px"></div>
    <p class="abs faq-text" style="top:915px">Lorem ipsum dolor sit amet, consectetur adipisicing elit, sed do eiusmod tempor incididunt ut labore et dolore magna aliqua. Ut enim ad minim veniam, quis.. <a>Read More</a></p>
    <div class="abs faq-sep" style="top:1006px"></div>
    <p class="abs faq-text" style="top:1017px">Lorem ipsum dolor sit amet, consectetur adipisicing elit, sed do eiusmod tempor incididunt ut labore et dolore magna aliqua. Ut enim ad minim veniam, quis.. <a>Read More</a></p>
    <div class="abs faq-sep" style="top:1100px"></div>

    <h3 class="abs small-title" style="left:318px;top:870px">Newsletter</h3>
    <div class="abs short-line" style="left:318px;top:898px"></div>
    <p class="abs nl-text">Sign up to our newsletter to receive discounts, news, and updates from <span>Varnok Corporation</span></p>
    <div class="abs field" style="top:975px">Name
      <svg width="10" height="11" viewBox="0 0 10 11"><circle cx="5" cy="3" r="2.6" fill="#aaa"/><path d="M0 11 C0 6 10 6 10 11 Z" fill="#aaa"/></svg>
    </div>
    <div class="abs field" style="top:1010px">Email
      <svg width="11" height="8" viewBox="0 0 11 8"><rect width="11" height="8" fill="#aaa"/><path d="M0 0 L5.5 4.5 L11 0" fill="none" stroke="#fff" stroke-width="1"/></svg>
    </div>
    <div class="abs subscribe">Subscribe</div>

    <h3 class="abs small-title" style="left:573px;top:870px">Testimonials</h3>
    <div class="abs short-line" style="left:573px;top:898px"></div>
    <div class="abs pager" style="left:757px;top:874px"><span></span><span></span></div>
    <div class="abs avatar" style="left:575px;top:918px" role="img" aria-label="Portrait of a client"></div>
    <div class="abs quote" style="top:923px"><span class="mark">“</span><p>Lorem ipsum dolor sit amet, consectetur adipisicing elit, sed do eiusmod tempor incididunt ut.</p><div class="who"><span>John Doe</span>, New York</div></div>
    <div class="abs t-sep" style="top:982px"></div>
    <div class="abs avatar" style="left:575px;top:1007px" role="img" aria-label="Portrait of a client"></div>
    <div class="abs quote" style="top:1012px"><span class="mark">“</span><p>Lorem ipsum dolor sit amet, consectetur adipisicing elit, sed do eiusmod tempor incididunt ut.</p><div class="who"><span>Jenna Doe</span>, New York</div></div>
    <div class="abs t-sep" style="top:1071px"></div>
  </section>

  <footer class="abs footer">
    <nav class="abs foot-nav"><span>Home</span><span>Services</span><span>Our Team</span><span>Insight Articles</span><span>Contact Us</span></nav>
    <p class="abs copy">Copyright©2014Varnok. All Rights Reserved</p>
    <div class="abs social" aria-label="Social links"><span></span><span></span><span></span><span></span></div>
  </footer>

</div>
</body>
</html>
```